Business card (AI file uploaded)

We need a business card design that is minimalist using existing logo (attached). Source files must be editable so we can make the same design with other names.

Screenshots included of a design I was working on to give you an idea of the style I would like. Looking for similar modern styles

Thanks

```html
<!DOCTYPE html>
<html lang="en">
<head>
<meta charset="utf-8">
<title>Marlow Law Group – Business Card</title>
<link rel="stylesheet" href="https://fonts.googleapis.com/css2?family=Marcellus&family=Lato:wght@400;700&display=swap">
<style>
  :root {
    --stage: #2a2a2a;
    --ink-black: #1d1b1c;
    --paper: #f4f4f4;
    --paper-shade: #d9d9d9;
    --text-dark: #2b2b2b;
    --text-mid: #555555;
    --text-light: #ffffff;
    --mark-grey: #4a4849;
  }
  * { margin: 0; padding: 0; box-sizing: border-box; }
  html, body { width: 1200px; height: 900px; overflow: hidden; }
  body {
    background: var(--stage);
    position: relative;
    font-family: "Lato", sans-serif;
  }
  .card {
    position: absolute;
    left: 280px;
    width: 640px;
    height: 366px;
    border-radius: 18px;
    overflow: hidden;
  }

  /* ---------- back side ---------- */
  .card-back {
    top: 56px;
    background: radial-gradient(ellipse at 50% 35%, #4a4748 0%, var(--ink-black) 60%);
    color: var(--text-light);
    text-align: center;
  }
  .card-back .brand-mark {
    position: absolute;
    top: 44px; left: 0; right: 0;
    display: flex; justify-content: center; align-items: center; gap: 10px;
    font-size: 22px; font-weight: 700; letter-spacing: 1px;
  }
  .brand-mark .dot {
    width: 22px; height: 22px; border-radius: 50%;
    background: currentColor;
  }
  .card-back .firm-name {
    position: absolute; top: 118px; left: 0; right: 0;
    font-family: "Marcellus", serif;
    font-size: 62px; letter-spacing: 3px; line-height: 1;
  }
  .card-back .firm-sub {
    position: absolute; top: 184px; left: 0; right: 0;
    font-family: "Marcellus", serif;
    font-size: 24px; letter-spacing: 8px;
  }
  .card-back .firm-sub small { font-size: 10px; letter-spacing: 1px; vertical-align: top; }
  .card-back .practice-areas {
    position: absolute; top: 258px; left: 0; right: 0;
    font-size: 16px; letter-spacing: 0.5px;
  }
  .base-band {
    position: absolute; left: 0; bottom: 0; width: 640px; height: 40px;
  }

  /* ---------- front side ---------- */
  .card-front {
    top: 478px;
    background: radial-gradient(ellipse at 55% 30%, #ffffff 0%, var(--paper) 45%, var(--paper-shade) 100%);
    color: var(--text-dark);
  }
  .card-front .monogram-field {
    position: absolute; left: -150px; top: -40px;
    width: 400px; height: 400px; border-radius: 50%;
    background: var(--mark-grey);
  }
  .card-front .brand-mark {
    position: absolute; top: 36px; right: 34px;
    display: flex; align-items: center; gap: 8px;
    font-size: 18px; font-weight: 700; color: var(--ink-black);
  }
  .contact-block {
    position: absolute; right: 34px; top: 116px;
    width: 330px; text-align: right;
  }
  .contact-block .person-name {
    font-size: 22px; line-height: 1.1; color: var(--text-dark); margin-right: 24px;
  }
  .contact-block .person-title {
    font-size: 13px; line-height: 1.2; color: var(--text-mid); margin-right: 24px; margin-top: 2px;
  }
  .contact-block .practice-areas {
    margin-top: 8px; margin-left: auto;
    width: 312px; text-align: left;
    font-size: 11px; font-weight: 700; line-height: 1.3; white-space: nowrap;
    padding-bottom: 5px;
    border-bottom: 2px solid var(--text-dark);
  }
  .contact-block ul { list-style: none; margin-top: 10px; }
  .contact-block li {
    display: flex; justify-content: flex-end; align-items: center; gap: 10px;
    font-size: 11.5px; color: #444; height: 21px; white-space: nowrap;
  }
  .contact-block li svg { width: 13px; height: 13px; fill: var(--ink-black); flex: none; }
</style>
</head>
<body>

<section class="card card-back" aria-label="Card back">
  <div class="brand-mark"><span class="dot"></span>Marlow</div>
  <div class="firm-name">MARLOW</div>
  <div class="firm-sub">LAW GROUP <small>PC</small></div>
  <div class="practice-areas">Real Estate &nbsp;|&nbsp; Bankruptcy &nbsp;|&nbsp; Social Security Disability</div>
  <svg class="base-band" viewBox="0 0 640 40" aria-hidden="true">
    <path d="M0 28 H180 L192 18 H448 L460 28 H640 V40 H0 Z" fill="#ffffff"/>
  </svg>
</section>

<section class="card card-front" aria-label="Card front">
  <div class="monogram-field" role="img" aria-label="Large decorative brand area"></div>
  <div class="brand-mark"><span class="dot"></span>Marlow</div>
  <div class="contact-block">
    <div class="person-name">Daniel Marlow</div>
    <div class="person-title">Attorney at Law</div>
    <div class="practice-areas">Real Estate | Bankruptcy | Social Security Disability</div>
    <ul>
      <li>410 Harbor Ave., Suite 200, Fairview, IL 60400
        <svg viewBox="0 0 16 16"><path d="M8 1a5 5 0 0 0-5 5c0 4 5 9 5 9s5-5 5-9a5 5 0 0 0-5-5zm0 7a2 2 0 1 1 0-4 2 2 0 0 1 0 4z"/></svg></li>
      <li>555.204.7719
        <svg viewBox="0 0 16 16"><path d="M5 1h6a1 1 0 0 1 1 1v12a1 1 0 0 1-1 1H5a1 1 0 0 1-1-1V2a1 1 0 0 1 1-1zm1 2v8h4V3zm2 9.5a.8.8 0 1 0 0 1.6.8.8 0 0 0 0-1.6z"/></svg></li>
      <li>555.318.6402
        <svg viewBox="0 0 16 16"><path d="M3 2h6l2 2v3H3zM1 8h14v6H1zm3 2v2h2v-2zm4 0v2h2v-2z"/></svg></li>
      <li>dmarlow@marlowlaw.com
        <svg viewBox="0 0 16 16"><path d="M1 3h14v10H1zm1.5 1.2L8 8.5l5.5-4.3z" fill-rule="evenodd"/></svg></li>
    </ul>
  </div>
  <svg class="base-band" viewBox="0 0 640 40" aria-hidden="true">
    <path d="M0 22 H150 L162 32 H640 V40 H0 Z" fill="#1d1b1c"/>
  </svg>
</section>

</body>
</html>
```